Banner Ad Design Project

I require banner ad designs with the below wording.

1. Join Today and Make Money Tomorrow. Unlimited Income. Click Here Now

2. I lost my job. Now I Make Over $5,000 Per Week From Home. You Can Too. Free Info, Apply Now

I require sizes: 300x250 and 728x90 and 468x60 and 120x240

The design should communicate legitimate, accredited, online business.

Industry/Entity Type

Business

Requirements
Should not have
• Creative attributes to avoid*
Phone numbers in creative
Creative with no click buttons
Interactive creative
Brand messaging with no call to action
Creative with long looping times

```html
<!DOCTYPE html>
<html lang="en">
<head>
<meta charset="utf-8">
<title>Banner Ad Set – Join Today / Make Money From Home</title>
<link rel="stylesheet" href="https://fonts.googleapis.com/css2?family=Oswald:wght@500;600&family=Roboto+Condensed:wght@400;500&family=PT+Serif:ital@1&display=swap">
<style>
  :root{
    --crimson:#c8174f;
    --crimson-deep:#a80f40;
    --ink:#151515;
    --charcoal:#4a4a4a;
    --gold:#ffe23a;
    --white:#ffffff;
    --stage-top:#7e7e7e;
    --stage-bottom:#cfcfcf;
    --photo-light:#eeeeee;
    --photo-mid:#c9c2bd;
    --photo-dark:#2a2a2a;
  }
  *{margin:0;padding:0;box-sizing:border-box}
  html,body{width:1200px;height:900px;overflow:hidden}
  body{
    background:radial-gradient(ellipse at 50% 60%, #c4c4c4 0%, transparent 70%),
               linear-gradient(180deg,var(--stage-top),var(--stage-bottom));
    font-family:"Roboto Condensed",Arial,sans-serif;
  }
  .board{position:absolute;left:0;top:0;width:1024px;height:768px;transform:scale(1.171875);transform-origin:0 0}
  .banner{position:absolute;overflow:hidden;box-shadow:0 1px 3px rgba(0,0,0,.25)}
  .banner > svg.bg{position:absolute;inset:0;width:100%;height:100%}
  .photo{position:absolute;background:linear-gradient(160deg,var(--photo-light) 0%,var(--photo-mid) 55%,var(--photo-dark) 100%)}
  .cash{position:absolute;border-radius:40% 40% 30% 30%;background:linear-gradient(120deg,#7fb38a 0%,#e6a35c 35%,#3f8fbf 60%,#d0684f 85%)}
  .copy{position:absolute;display:flex;flex-direction:column;align-items:center;justify-content:center;text-align:center;line-height:1.05}
  .w{color:var(--white)}
  .r{color:var(--crimson)}
  .gold{color:var(--gold);font-family:"Oswald",Impact,sans-serif;font-weight:600;text-shadow:0 1px 1px rgba(0,0,0,.35)}
  .serif{font-family:"PT Serif",Georgia,serif;font-style:italic;color:var(--white)}
  .pill{position:absolute;background:var(--white);color:var(--ink);display:flex;align-items:center;justify-content:center;border-radius:999px 0 0 999px;font-weight:500}

  /* positions */
  .lost-468{left:293px;top:99px;width:468px;height:60px}
  .join-468{left:293px;top:180px;width:468px;height:60px}
  .join-300{left:63px;top:271px;width:300px;height:250px}
  .lost-300{left:377px;top:271px;width:300px;height:250px}
  .lost-120{left:711px;top:276px;width:120px;height:240px}
  .join-120{left:853px;top:276px;width:120px;height:240px}
  .lost-728{left:137px;top:545px;width:728px;height:90px}
  .join-728{left:137px;top:650px;width:728px;height:90px}
</style>
</head>
<body>
<div class="board">

  <!-- 468x60 : lost job -->
  <div class="banner lost-468">
    <svg class="bg" viewBox="0 0 468 60" preserveAspectRatio="none">
      <rect width="468" height="60" fill="#fff"/>
      <path d="M112,0 L284,0 L294,30 L284,60 L104,60 C94,40 98,15 112,0Z" fill="var(--crimson)"/>
      <path d="M452,0 L468,0 L468,60 L452,60 L461,30Z" fill="var(--crimson)"/>
    </svg>
    <div class="photo" style="left:0;top:0;width:104px;height:60px" role="img" aria-label="Photo of a joyful woman celebrating with raised arm"></div>
    <div class="copy" style="left:110px;top:2px;width:180px;height:56px">
      <span class="w" style="font-size:12px">I lost my job Now I Make Over</span>
      <span class="gold" style="font-size:17px">$5,000 Per Week</span>
      <span class="w" style="font-size:11px">From Home</span>
    </div>
    <div class="copy r" style="left:296px;top:4px;width:156px;height:52px;font-size:17px;line-height:1.3">
      <span>You Can Too</span><span>Free Info, Apply Now</span>
    </div>
  </div>

  <!-- 468x60 : join today -->
  <div class="banner join-468">
    <svg class="bg" viewBox="0 0 468 60" preserveAspectRatio="none">
      <defs><linearGradient id="dk1" x1="0" x2="1"><stop offset="0" stop-color="var(--ink)"/><stop offset="1" stop-color="var(--charcoal)"/></linearGradient></defs>
      <rect width="468" height="60" fill="url(#dk1)"/>
      <path d="M270,0 L468,0 L468,60 L256,60 C268,40 262,15 270,0Z" fill="var(--crimson)"/>
    </svg>
    <div class="photo" style="left:0;top:0;width:44px;height:60px" role="img" aria-label="Portrait of a smiling businesswoman in glasses"></div>
    <div class="copy" style="left:44px;top:3px;width:140px;height:54px;align-items:flex-start">
      <span class="gold" style="font-size:27px">Join Today</span>
      <span class="w" style="font-size:12px">&amp; Make Money&nbsp; Tomorrow</span>
    </div>
    <div class="cash" style="left:196px;top:2px;width:92px;height:58px" role="img" aria-label="Hand holding a fan of banknotes"></div>
    <div class="copy serif" style="left:284px;top:4px;width:90px;height:52px;font-size:20px">
      <span>Unlimited</span><span>Income</span>
    </div>
    <div class="pill" style="left:378px;top:14px;width:90px;height:32px;font-size:13px">Click Here Now</div>
  </div>

  <!-- 300x250 : join today -->
  <div class="banner join-300">
    <svg class="bg" viewBox="0 0 300 250" preserveAspectRatio="none">
      <defs><linearGradient id="dk2" x1="0" y1="0" x2="0" y2="1"><stop offset="0" stop-color="var(--ink)"/><stop offset="1" stop-color="var(--charcoal)"/></linearGradient></defs>
      <rect width="300" height="250" fill="url(#dk2)"/>
      <path d="M100,196 C170,190 250,170 300,150 L300,250 L100,250Z" fill="#fff"/>
      <path d="M100,204 C170,198 250,178 300,160 L300,250 L100,250Z" fill="var(--crimson)"/>
    </svg>
    <div class="photo" style="left:0;top:0;width:120px;height:250px" role="img" aria-label="Portrait of a smiling businesswoman in glasses and dark blazer"></div>
    <div class="copy" style="left:100px;top:12px;width:200px;height:110px">
      <span class="gold" style="font-size:38px">Join Today</span>
      <span class="w" style="font-size:16px;margin-top:6px">&amp; Make Money&nbsp; Tomorrow</span>
      <span class="serif" style="font-size:22px;margin-top:12px">Unlimited Income</span>
    </div>
    <div class="cash" style="left:128px;top:148px;width:118px;height:74px" role="img" aria-label="Hand holding a fan of banknotes"></div>
    <div class="pill" style="left:170px;top:202px;width:130px;height:38px;font-size:16px">Click Here Now</div>
  </div>

  <!-- 300x250 : lost job -->
  <div class="banner lost-300">
    <svg class="bg" viewBox="0 0 300 250" preserveAspectRatio="none">
      <rect width="300" height="250" fill="var(--crimson)"/>
    </svg>
    <div class="photo" style="left:45px;top:0;width:255px;height:98px;border-radius:0 0 0 100% / 0 0 0 100%" role="img" aria-label="Photo of a joyful woman celebrating with raised arm"></div>
    <div class="copy" style="left:0;top:105px;width:300px;height:95px">
      <span class="w" style="font-size:19px">I lost my job. Now I Make Over</span>
      <span class="gold" style="font-size:28px;margin:2px 0">$5,000 Per Week</span>
      <span class="w" style="font-size:19px">From Home</span>
    </div>
    <svg style="position:absolute;left:0;top:0;width:300px;height:250px" viewBox="0 0 300 250">
      <path d="M5,214 Q150,198 295,214 L295,245 L5,245Z" fill="#fff"/>
    </svg>
    <div class="copy r" style="left:5px;top:212px;width:290px;height:33px;font-size:18px">You Can Too. Free Info, Apply Now</div>
  </div>

  <!-- 120x240 : lost job -->
  <div class="banner lost-120">
    <svg class="bg" viewBox="0 0 120 240" preserveAspectRatio="none">
      <rect width="120" height="240" fill="var(--crimson)"/>
      <rect x="5" y="214" width="110" height="22" fill="#fff"/>
    </svg>
    <div class="photo" style="left:25px;top:0;width:95px;height:80px;border-radius:0 0 0 100% / 0 0 0 100%" role="img" aria-label="Photo of a joyful woman celebrating with raised arm"></div>
    <div class="copy" style="left:0;top:86px;width:120px;height:124px">
      <span class="w" style="font-size:14px;line-height:1.5">I lost my job</span>
      <span class="w" style="font-size:14px;line-height:1.3">Now I Make Over</span>
      <span class="gold" style="font-size:24px;line-height:1.1">$5,000</span>
      <span class="gold" style="font-size:24px;line-height:1.1">Per Week</span>
      <span class="w" style="font-size:14px;line-height:1.5">From Home</span>
    </div>
    <div class="copy r" style="left:5px;top:214px;width:110px;height:22px;font-size:14px">Apply Now</div>
  </div>

  <!-- 120x240 : join today -->
  <div class="banner join-120">
    <svg class="bg" viewBox="0 0 120 240" preserveAspectRatio="none">
      <defs><linearGradient id="dk3" x1="0" y1="0" x2="0" y2="1"><stop offset="0" stop-color="var(--ink)"/><stop offset="1" stop-color="var(--charcoal)"/></linearGradient></defs>
      <rect width="120" height="240" fill="url(#dk3)"/>
      <path d="M0,206 C40,200 90,190 120,176 L120,240 L0,240Z" fill="#fff"/>
      <path d="M0,212 C40,206 90,196 120,183 L120,240 L0,240Z" fill="var(--crimson)"/>
    </svg>
    <div class="copy" style="left:0;top:8px;width:120px;height:136px">
      <span class="gold" style="font-size:22px">Join Today</span>
      <span class="w" style="font-size:14px;margin-top:6px;line-height:1.4">&amp; Make Money<br>Tomorrow</span>
      <span class="serif" style="font-size:20px;margin-top:4px">Unlimited<br>Income</span>
    </div>
    <div class="cash" style="left:18px;top:146px;width:92px;height:54px" role="img" aria-label="Hand holding a fan of banknotes"></div>
    <div class="copy w" style="left:0;top:214px;width:120px;height:24px;font-size:13px">Click Here Now</div>
  </div>

  <!-- 728x90 : lost job -->
  <div class="banner lost-728">
    <svg class="bg" viewBox="0 0 728 90" preserveAspectRatio="none">
      <rect width="728" height="90" fill="#fff"/>
      <path d="M170,0 L436,0 L448,45 L436,90 L156,90 C142,60 148,22 170,0Z" fill="var(--crimson)"/>
      <path d="M706,0 L728,0 L728,90 L706,90 L718,45Z" fill="var(--crimson)"/>
    </svg>
    <div class="photo" style="left:0;top:0;width:156px;height:90px" role="img" aria-label="Photo of a joyful woman celebrating with raised arm"></div>
    <div class="copy" style="left:160px;top:4px;width:276px;height:82px">
      <span class="w" style="font-size:18px">I lost my job Now I Make Over</span>
      <span class="gold" style="font-size:27px;margin:2px 0">$5,000 Per Week</span>
      <span class="w" style="font-size:17px">From Home</span>
    </div>
    <div class="copy r" style="left:450px;top:6px;width:254px;height:78px;font-size:23px;line-height:1.4">
      <span>You Can Too</span><span>Free Info, Apply Now</span>
    </div>
  </div>

  <!-- 728x90 : join today -->
  <div class="banner join-728">
    <svg class="bg" viewBox="0 0 728 90" preserveAspectRatio="none">
      <defs><linearGradient id="dk4" x1="0" x2="1"><stop offset="0" stop-color="var(--ink)"/><stop offset="1" stop-color="var(--charcoal)"/></linearGradient></defs>
      <rect width="728" height="90" fill="url(#dk4)"/>
      <path d="M438,0 L728,0 L728,90 L420,90 C436,60 430,22 438,0Z" fill="var(--crimson)"/>
    </svg>
    <div class="photo" style="left:0;top:0;width:64px;height:90px" role="img" aria-label="Portrait of a smiling businesswoman in glasses"></div>
    <div class="copy" style="left:70px;top:6px;width:220px;height:78px">
      <span class="gold" style="font-size:44px">Join Today</span>
      <span class="w" style="font-size:19px">&amp; Make Money&nbsp; Tomorrow</span>
    </div>
    <div class="cash" style="left:292px;top:4px;width:150px;height:86px" role="img" aria-label="Hand holding a fan of banknotes"></div>
    <div class="copy serif" style="left:440px;top:8px;width:142px;height:74px;font-size:29px">
      <span>Unlimited</span><span>Income</span>
    </div>
    <div class="pill" style="left:588px;top:20px;width:140px;height:52px;font-size:20px">Click Here Now</div>
  </div>

</div>
</body>
</html>
```